CD-Cover gestalten
Zielgruppe
12 - 55, hauptsächlich Frauen... oder Menschen, die schön gestaltete Dinge schätzen... Hauptsache das Cover ist schön...
Aufgabenstellung
Gesucht wird ein Cover für eine CD mit:
1. Weihnachtsmotiv. Es kann klassisch mit pausbäckigem Weihnachtsmann etc., Tannenbaum, von mir aus Rentier etc. sein, lustig oder sehr modern... es sollte und kann "Fröhliche Weihnachten" darauf stehen, von mir aus in verschiedenen Schriftarten oder/und Sprachen.
2. Hochzeitsmotiv (von klassisch traditionell mit Blümelein, Vögelein, Brautpaar... bis lustig oder modern...)
3. Babymotiv (für Jungen und Mädchen geeignet, ebenfalls klassisch mit typischen Attributen, lustig oder modern...)
Es soll später Fotos oder Musik auf die CD gespeichert/gebrannt werden können...

```html
<!DOCTYPE html>
<html lang="de">
<head>
<meta charset="utf-8">
<title>Fröhliche Weihnachten – CD-Label</title>
<link rel="stylesheet" href="https://fonts.googleapis.com/css2?family=Pinyon+Script&display=swap">
<style>
  :root {
    --page-bg: #ffffff;
    --disc-top: #040203;
    --disc-dark: #1a0406;
    --disc-mid: #5a1012;
    --disc-bottom: #d3151b;
    --hole-fill: #ffffff;
    --hole-rim: #1c1f4a;
    --ornament-rose: #b4555b;
    --ornament-cream: #f1d6c4;
    --silver: #d9d4cf;
    --sparkle-white: #fffaf0;
    --flake-gold: #f2df7a;
    --flake-green: #5fa35a;
    --flake-red: #d8213a;
    --flake-blue: #3e5fc4;
    --flake-cyan: #5fc3de;
    --flake-orange: #f07a2a;
    --flake-purple: #9a79c6;
    --greeting: #ffffff;
    --greeting-shade: #3a0b0d;
  }
  html, body {
    margin: 0;
    padding: 0;
    width: 1161px;
    height: 1200px;
    overflow: hidden;
    background: var(--page-bg);
  }
  .cd-label { position: relative; width: 1161px; height: 1200px; }
  .cd-label__art { position: absolute; inset: 0; width: 1161px; height: 1200px; }
  .cd-label__greeting {
    position: absolute;
    left: 116px;
    top: 642px;
    margin: 0;
    font-family: "Pinyon Script", cursive;
    font-weight: 400;
    font-size: 86px;
    line-height: 0.92;
    color: var(--greeting);
    text-shadow: 2px 2px 0 var(--greeting-shade), -1px -1px 0 var(--greeting-shade);
    transform: rotate(-7deg);
    transform-origin: left top;
  }
  .cd-label__greeting span { display: block; }
  .cd-label__greeting .line-1 { margin-left: 10px; }
</style>
</head>
<body>
<main class="cd-label">
  <svg class="cd-label__art" viewBox="0 0 1161 1200" xmlns="http://www.w3.org/2000/svg">
    <defs>
      <linearGradient id="disc-gradient" x1="0" y1="0" x2="0" y2="1">
        <stop offset="0" stop-color="var(--disc-top)"/>
        <stop offset="0.22" stop-color="var(--disc-top)"/>
        <stop offset="0.4" stop-color="var(--disc-dark)"/>
        <stop offset="0.62" stop-color="var(--disc-mid)"/>
        <stop offset="1" stop-color="var(--disc-bottom)"/>
      </linearGradient>
      <radialGradient id="g-sparkle"><stop offset="0" stop-color="var(--sparkle-white)" stop-opacity="1"/><stop offset="0.2" stop-color="var(--sparkle-white)" stop-opacity="0.6"/><stop offset="1" stop-color="var(--sparkle-white)" stop-opacity="0"/></radialGradient>
      <radialGradient id="g-silver"><stop offset="0" stop-color="var(--silver)" stop-opacity="0.4"/><stop offset="1" stop-color="var(--silver)" stop-opacity="0"/></radialGradient>
      <radialGradient id="g-rose"><stop offset="0" stop-color="var(--ornament-rose)" stop-opacity="0.75"/><stop offset="1" stop-color="var(--ornament-rose)" stop-opacity="0"/></radialGradient>
      <radialGradient id="g-cream"><stop offset="0" stop-color="var(--ornament-cream)" stop-opacity="0.95"/><stop offset="0.6" stop-color="var(--ornament-cream)" stop-opacity="0.6"/><stop offset="1" stop-color="var(--ornament-cream)" stop-opacity="0"/></radialGradient>
      <radialGradient id="g-gold"><stop offset="0" stop-color="var(--flake-gold)"/><stop offset="0.5" stop-color="var(--flake-gold)" stop-opacity="0.7"/><stop offset="1" stop-color="var(--flake-gold)" stop-opacity="0"/></radialGradient>
      <radialGradient id="g-green"><stop offset="0" stop-color="var(--flake-green)"/><stop offset="0.5" stop-color="var(--flake-green)" stop-opacity="0.7"/><stop offset="1" stop-color="var(--flake-green)" stop-opacity="0"/></radialGradient>
      <radialGradient id="g-red"><stop offset="0" stop-color="var(--flake-red)"/><stop offset="0.5" stop-color="var(--flake-red)" stop-opacity="0.7"/><stop offset="1" stop-color="var(--flake-red)" stop-opacity="0"/></radialGradient>
      <radialGradient id="g-blue"><stop offset="0" stop-color="var(--flake-blue)"/><stop offset="0.5" stop-color="var(--flake-blue)" stop-opacity="0.7"/><stop offset="1" stop-color="var(--flake-blue)" stop-opacity="0"/></radialGradient>
      <radialGradient id="g-cyan"><stop offset="0" stop-color="var(--flake-cyan)"/><stop offset="0.5" stop-color="var(--flake-cyan)" stop-opacity="0.7"/><stop offset="1" stop-color="var(--flake-cyan)" stop-opacity="0"/></radialGradient>
      <radialGradient id="g-orange"><stop offset="0" stop-color="var(--flake-orange)"/><stop offset="0.5" stop-color="var(--flake-orange)" stop-opacity="0.7"/><stop offset="1" stop-color="var(--flake-orange)" stop-opacity="0"/></radialGradient>
      <radialGradient id="g-purple"><stop offset="0" stop-color="var(--flake-purple)"/><stop offset="0.5" stop-color="var(--flake-purple)" stop-opacity="0.7"/><stop offset="1" stop-color="var(--flake-purple)" stop-opacity="0"/></radialGradient>
      <clipPath id="disc-clip"><circle cx="590" cy="622" r="550"/></clipPath>
    </defs>

    <circle class="disc" cx="590" cy="622" r="550" fill="url(#disc-gradient)"/>

    <g class="disc__decor" clip-path="url(#disc-clip)">
      <g class="decor__swirls" role="img" aria-label="Silberne Glitzerwirbel im dunklen oberen Bereich und rechts">
        <ellipse cx="480" cy="200" rx="260" ry="120" fill="url(#g-silver)"/>
        <ellipse cx="150" cy="470" rx="110" ry="140" fill="url(#g-silver)"/>
        <ellipse cx="1010" cy="480" rx="130" ry="200" fill="url(#g-silver)"/>
        <ellipse cx="880" cy="280" rx="170" ry="110" fill="url(#g-silver)"/>
      </g>

      <g class="decor__bow-flakes" role="img" aria-label="Große rosa Schneeflocken mit Schleifen um das Mittelloch und im unteren Bereich">
        <ellipse cx="600" cy="440" rx="240" ry="160" fill="url(#g-rose)"/>
        <ellipse cx="340" cy="560" rx="150" ry="120" fill="url(#g-rose)" opacity="0.8"/>
        <ellipse cx="560" cy="860" rx="200" ry="150" fill="url(#g-rose)" opacity="0.6"/>
        <ellipse cx="880" cy="820" rx="200" ry="160" fill="url(#g-rose)" opacity="0.55"/>
        <ellipse cx="180" cy="760" rx="130" ry="120" fill="url(#g-rose)" opacity="0.5"/>
        <ellipse cx="640" cy="1060" rx="170" ry="90" fill="url(#g-rose)" opacity="0.45"/>
      </g>

      <g class="decor__flakes" role="img" aria-label="Bunte kleine Schneeflocken verstreut über die Scheibe">
        <circle cx="383" cy="158" r="48" fill="url(#g-green)"/>
        <circle cx="293" cy="267" r="28" fill="url(#g-gold)"/>
        <circle cx="720" cy="177" r="46" fill="url(#g-gold)"/>
        <circle cx="818" cy="192" r="26" fill="url(#g-red)"/>
        <circle cx="927" cy="258" r="28" fill="url(#g-orange)"/>
        <circle cx="323" cy="387" r="28" fill="url(#g-green)"/>
        <circle cx="222" cy="417" r="36" fill="url(#g-gold)"/>
        <circle cx="108" cy="458" r="26" fill="url(#g-orange)"/>
        <circle cx="173" cy="528" r="40" fill="url(#g-blue)"/>
        <circle cx="330" cy="483" r="40" fill="url(#g-cyan)"/>
        <circle cx="293" cy="585" r="52" fill="url(#g-red)" opacity="0.7"/>
        <circle cx="582" cy="428" r="50" fill="url(#g-red)"/>
        <circle cx="705" cy="435" r="40" fill="url(#g-gold)"/>
        <circle cx="675" cy="515" r="26" fill="url(#g-green)"/>
        <circle cx="807" cy="558" r="46" fill="url(#g-purple)"/>
        <circle cx="888" cy="563" r="30" fill="url(#g-blue)"/>
        <circle cx="1071" cy="488" r="24" fill="url(#g-red)"/>
        <circle cx="948" cy="653" r="50" fill="url(#g-green)" opacity="0.7"/>
        <circle cx="855" cy="650" r="80" fill="url(#g-purple)" opacity="0.6"/>
        <circle cx="68" cy="645" r="36" fill="url(#g-gold)"/>
        <circle cx="1076" cy="728" r="38" fill="url(#g-gold)"/>
        <circle cx="450" cy="1058" r="80" fill="url(#g-purple)" opacity="0.7"/>
      </g>

      <g class="decor__sparkles" role="img" aria-label="Funkelnde Lichtsterne">
        <circle cx="398" cy="270" r="40" fill="url(#g-sparkle)"/>
        <circle cx="652" cy="147" r="34" fill="url(#g-sparkle)"/>
        <circle cx="818" cy="292" r="38" fill="url(#g-sparkle)"/>
        <circle cx="862" cy="225" r="22" fill="url(#g-sparkle)"/>
        <circle cx="982" cy="315" r="24" fill="url(#g-sparkle)"/>
        <circle cx="760" cy="120" r="20" fill="url(#g-sparkle)"/>
        <circle cx="387" cy="615" r="36" fill="url(#g-sparkle)"/>
        <circle cx="607" cy="772" r="34" fill="url(#g-sparkle)"/>
        <circle cx="945" cy="787" r="30" fill="url(#g-sparkle)"/>
        <circle cx="780" cy="1020" r="40" fill="url(#g-sparkle)"/>
        <circle cx="285" cy="870" r="26" fill="url(#g-sparkle)"/>
        <circle cx="200" cy="320" r="22" fill="url(#g-sparkle)"/>
        <circle cx="840" cy="610" r="20" fill="url(#g-sparkle)"/>
      </g>

      <g class="decor__flourish" role="img" aria-label="Cremefarbene florale Ranke unter dem Schriftzug">
        <ellipse cx="380" cy="890" rx="200" ry="70" fill="url(#g-cream)"/>
        <ellipse cx="470" cy="840" rx="80" ry="50" fill="url(#g-cream)" opacity="0.8"/>
        <ellipse cx="430" cy="950" rx="110" ry="40" fill="url(#g-cream)" opacity="0.7"/>
      </g>
    </g>

    <circle class="disc__hole" cx="591" cy="624" r="96" fill="var(--hole-fill)" stroke="var(--hole-rim)" stroke-width="5"/>
  </svg>

  <h1 class="cd-label__greeting">
    <span class="line-1">Fröhliche</span>
    <span class="line-2">Weihnachten</span>
  </h1>
</main>
</body>
</html>
```